We require a banner design for a 53' x 10' trailer for a future development to be displayed on the side of the highway. The development name is 712 35 Commerce Park, logo is attached. This is an industrial future development. Please also include the RLW Group logo and MERO Development logos as well.

Industry/Entity Type

Real Estate / Construction / Developer / Industrial Future Development

Requirements
Must have
• Logos provided

```html
<!DOCTYPE html>
<html lang="en">
<head>
<meta charset="utf-8">
<title>712 35 Commerce Park – Trailer Banner Options</title>
<link href="https://fonts.googleapis.com/css2?family=Montserrat:wght@500;700;800&display=swap" rel="stylesheet">
<style>
  :root {
    --board: #3fdfb8;
    --shadow: rgba(10, 80, 60, 0.55);
    --panel: #ffffff;
    --ink: #231f20;
    --paper: #ffffff;
  }
  * { margin: 0; padding: 0; box-sizing: border-box; }
  html, body {
    width: 1200px;
    height: 500px;
    overflow: hidden;
    background: var(--board);
    font-family: "Montserrat", sans-serif;
  }
  .board { position: relative; width: 1200px; height: 500px; }

  .banner {
    position: absolute;
    left: 53px;
    width: 1088px;
    height: 206px;
    background: var(--panel);
    box-shadow: -6px 14px 18px var(--shadow);
    overflow: hidden;
  }
  .banner--light { top: 34px; }
  .banner--dark { top: 262px; left: 49px; width: 1092px; }

  .chevron-panel {
    position: absolute;
    left: 0; top: 0;
    width: 356px; height: 206px;
  }
  .chevron-panel polygon { fill: var(--ink); }

  .project-name {
    position: absolute;
    top: 18px;
    left: 59px;
    color: var(--ink);
  }
  .banner--dark .project-name { left: 60px; color: var(--paper); }
  .project-name__number {
    display: block;
    font-weight: 800;
    font-size: 84px;
    line-height: 0.8;
    letter-spacing: 1px;
  }
  .project-name__label {
    display: block;
    margin-top: 14px;
    font-weight: 500;
    font-size: 22px;
    letter-spacing: 2px;
    white-space: nowrap;
  }

  .partner {
    position: absolute;
    top: 50%;
    transform: translateY(-50%);
    font-weight: 700;
    font-size: 32px;
    color: var(--ink);
    white-space: nowrap;
  }
  .banner--light .partner--rlw { left: 370px; }
  .banner--dark .partner--rlw { left: 430px; }
  .banner--light .partner--mero { left: 700px; }
  .banner--dark .partner--mero { left: 730px; }
</style>
</head>
<body>
<main class="board">

  <section class="banner banner--light">
    <div class="project-name">
      <span class="project-name__number">712<br>35</span>
      <span class="project-name__label">COMMERCE PARK</span>
    </div>
    <p class="partner partner--rlw">RLW Group</p>
    <p class="partner partner--mero">MERO Development</p>
  </section>

  <section class="banner banner--dark">
    <svg class="chevron-panel" viewBox="0 0 356 206" aria-hidden="true">
      <polygon points="0,0 314,0 353,103 314,206 0,206"/>
    </svg>
    <div class="project-name">
      <span class="project-name__number">712<br>35</span>
      <span class="project-name__label">COMMERCE PARK</span>
    </div>
    <p class="partner partner--rlw">RLW Group</p>
    <p class="partner partner--mero">MERO Development</p>
  </section>

</main>
</body>
</html>
```